Business Cards Design for the electrical wholesaler: clean bold dynamic :)

We need a business card design that would follow our latest brand guidelines. As an electrical wholesaler we want to bring a fresh look and feel into the industry. The design should be clean bold and dynamic. It should come alive with the renewed energy of our green colour. Our grey colour should keep things balanced and complement the notion of maturity and responsibility. We employ Lato as a corporate font however are not bound by this font and we’re open to interpretation here.

Target Market(s)

Electrical contractors

Industry/Entity Type

Business

Contact Information for Business Card

Logo
Name & Surname: Olena Dovbush
Job Title: Director of Marketing
Email: helen.dovbush@mailvane.example
Cell phone: 780.555.0142
Address: 20917 - 87 Ave. Edmonton, AB, Canada. T6K 2R8
Business Phone: 780.555.0187
Website: www.qorvil.example

Font styles to use
Other font styles liked:
• Lato

Requirements
Must have
• Logo & website
Nice to have
• Brand elements - some of them you may find in the attached Brand Guidelines (e.g. three lines on the background signifying "W")

```html
<!DOCTYPE html>
<html lang="en">
<head>
<meta charset="utf-8">
<title>Qorvil business card</title>
<link rel="stylesheet" href="https://fonts.googleapis.com/css2?family=Work+Sans:wght@400;500;600&display=swap">
<style>
  :root {
    --backdrop: #141414;
    --card: #262626;
    --card-edge: #2e2e2e;
    --green: #7cc242;
    --grey-mark: #8a8a8a;
    --white: #f2f2f2;
    --icon: #7cc242;
  }
  * { margin: 0; padding: 0; box-sizing: border-box; }
  html, body { width: 1200px; height: 900px; overflow: hidden; }
  body {
    background: var(--backdrop);
    font-family: "Work Sans", Arial, sans-serif;
    position: relative;
  }
  .card {
    position: absolute;
    left: 250px;
    width: 700px;
    height: 400px;
    background: linear-gradient(135deg, var(--card) 0%, var(--card-edge) 100%);
    border-bottom: 9px solid var(--green);
  }
  .card--front { top: 30px; }
  .card--back { top: 465px; }

  .wordmark {
    font-weight: 500;
    letter-spacing: 1px;
    line-height: 1;
    display: flex;
    align-items: center;
    gap: 16px;
    white-space: nowrap;
  }
  .wordmark__dot {
    width: 26px; height: 26px;
    border-radius: 50%;
    background: currentColor;
  }
  .card--front .wordmark {
    position: absolute;
    left: 50%; top: 50%;
    transform: translate(-50%, -50%);
    font-size: 84px;
    color: var(--grey-mark);
  }
  .card--back .wordmark {
    position: absolute;
    left: 50px; top: 165px;
    font-size: 56px;
    color: var(--white);
  }
  .card--back .wordmark__dot { background: var(--green); width: 20px; height: 20px; }

  .divider {
    position: absolute;
    left: 340px; top: 100px;
    width: 2px; height: 200px;
    background: var(--green);
  }
  .contact {
    position: absolute;
    left: 366px; top: 98px;
    width: 320px;
    color: var(--white);
  }
  .contact__name {
    color: var(--green);
    font-size: 26px;
    font-weight: 600;
    letter-spacing: 1px;
    line-height: 1.2;
  }
  .contact__role {
    font-size: 17px;
    letter-spacing: 0.5px;
    margin-bottom: 12px;
  }
  .contact__address {
    font-size: 15px;
    letter-spacing: 0.5px;
    line-height: 1.35;
    margin-bottom: 10px;
  }
  .contact__line {
    display: flex;
    align-items: center;
    gap: 10px;
    font-size: 15px;
    letter-spacing: 0.5px;
    line-height: 1.45;
    white-space: nowrap;
  }
  .contact__line svg { width: 13px; height: 13px; flex: none; }
  .contact__label { color: var(--green); font-size: 12px; font-weight: 600; width: 13px; text-align: center; flex: none; }
</style>
</head>
<body>
  <section class="card card--front">
    <div class="wordmark"><span class="wordmark__dot"></span>qorvil</div>
  </section>

  <section class="card card--back">
    <div class="wordmark"><span class="wordmark__dot"></span>qorvil</div>
    <div class="divider"></div>
    <div class="contact">
      <p class="contact__name">Olena Dovbush</p>
      <p class="contact__role">Director of Marketing</p>
      <p class="contact__address">20917 - 87 Ave. Edmonton, AB,<br>Canada. T6K 2R8</p>
      <p class="contact__line">
        <svg viewBox="0 0 16 16" aria-hidden="true"><path fill="var(--icon)" d="M3.5 1l2.5 3-1.5 2c.8 2 2.5 3.7 4.5 4.5l2-1.5 3 2.5-1.5 2.5C7 14 2 9 1 2.5z"/></svg>
        780.555.0187
      </p>
      <p class="contact__line">
        <span class="contact__label">C</span>
        780.555.0142
      </p>
      <p class="contact__line">
        <svg viewBox="0 0 16 16" aria-hidden="true"><rect x="1.5" y="3.5" width="13" height="9" fill="none" stroke="var(--icon)" stroke-width="1.6"/><path d="M1.5 3.5L8 9l6.5-5.5" fill="none" stroke="var(--icon)" stroke-width="1.6"/></svg>
        helen.dovbush@mailvane.example
      </p>
      <p class="contact__line">
        <svg viewBox="0 0 16 16" aria-hidden="true"><g fill="none" stroke="var(--icon)" stroke-width="1.4"><circle cx="8" cy="8" r="6.3"/><ellipse cx="8" cy="8" rx="2.8" ry="6.3"/><path d="M1.7 8h12.6M3 4.5h10M3 11.5h10"/></g></svg>
        www.qorvil.example
      </p>
    </div>
  </section>
</body>
</html>
```